Bright Lane Collective needs updated website.

Our current website was designed on wix.com. (www.brightlanecollective.example).
We would like something a little more customized for what our company offers. Bright Lane Collective is a company specializing in connecting consumers with trustworthy and affordable service professionals. We need the website to be approachable and easy to use, while conveying our "Bright Lane" reputation.
Reason: Our project is now guaranteed. Please send your ideas. Thank you!
Target Market(s)
Homeowners
Industry/Entity Type
It Company
Look and feel

```html
<!DOCTYPE html>
<html lang="en">
<head>
<meta charset="utf-8">
<title>Bright Lane Collective</title>
<link rel="stylesheet" href="https://fonts.googleapis.com/css2?family=Roboto:wght@300;400;700&family=Source+Sans+3:wght@400;600;700&display=swap">
<style>
  :root {
    --brand-blue: #1a7cc6;
    --brand-blue-deep: #0f6db6;
    --hero-light: #dfe9f2;
    --text-dark: #1e1e1e;
    --text-grey: #5a5a5a;
    --heading-grey: #6b6b6b;
    --footer-bg: #2f2f31;
    --footer-text: #b9b9b9;
    --footer-icon: #9a9a9a;
    --base-bar: #00325f;
    --white: #ffffff;
  }
  * { box-sizing: border-box; margin: 0; padding: 0; }
  html, body { width: 1107px; height: 1200px; overflow: hidden; background: var(--white); }
  body { position: relative; font-family: "Source Sans 3", sans-serif; color: var(--text-dark); }

  .site-header { position: absolute; top: 0; left: 0; width: 1107px; height: 166px; }
  .brand { position: absolute; display: flex; align-items: center; gap: 12px; }
  .site-header .brand { left: 102px; top: 42px; }
  .brand-dot { width: 66px; height: 66px; border-radius: 50%; background: var(--brand-blue); flex: none; }
  .brand-name { font-family: "Roboto", sans-serif; font-weight: 700; font-size: 34px; color: var(--brand-blue); white-space: nowrap; letter-spacing: -0.5px; }

  .main-nav { position: absolute; right: 102px; top: 64px; display: flex; align-items: center; font-family: "Roboto", sans-serif; font-weight: 300; font-size: 24px; color: var(--text-grey); }
  .main-nav a { color: inherit; text-decoration: none; }
  .main-nav .divider { display: inline-block; width: 2px; height: 12px; background: var(--text-grey); margin: 4px 18px 0; }

  .hero { position: absolute; top: 166px; left: 0; width: 1107px; height: 331px; background: var(--brand-blue); overflow: hidden; }
  .hero-photo { position: absolute; top: 0; right: 0; width: 560px; height: 331px;
    background: linear-gradient(90deg, var(--brand-blue) 0%, #5f9fd3 30%, #b8d0e6 65%, var(--hero-light) 100%); }
  .hero-copy { position: absolute; left: 56px; top: 30px; width: 496px; color: var(--white); text-align: center; }
  .hero-title { font-size: 34px; font-weight: 400; margin-bottom: 24px; padding-left: 0; }
  .hero-copy p { font-size: 19px; line-height: 24px; margin-bottom: 16px; }
  .hero-copy strong { font-weight: 700; }

  .features { position: absolute; top: 497px; left: 0; width: 1107px; height: 465px; }
  .feature { position: absolute; top: 43px; width: 240px; text-align: center; }
  .feature-icon { width: 52px; height: 52px; margin: 0 auto; display: block; }
  .feature-title { font-family: "Roboto", sans-serif; font-weight: 300; font-size: 24px; color: var(--heading-grey); margin-top: 32px; height: 60px; }
  .feature-text { font-size: 14.5px; line-height: 18.2px; width: 200px; margin: 0 auto; }
  .service-list { list-style: none; text-align: left; width: 200px; margin: 5px 0 0 -6px; font-size: 14.5px; line-height: 18.2px; }
  .service-list li { position: relative; padding-left: 25px; }
  .service-list li::before { content: ""; position: absolute; left: 0; top: 5px; width: 8px; height: 8px; border-radius: 50%; background: var(--brand-blue); }
  .read-more { position: absolute; top: 382px; width: 99px; height: 29px; border-radius: 5px; background: var(--brand-blue); border: 1px solid var(--brand-blue-deep);
    color: var(--white); font-weight: 600; font-size: 14px; line-height: 27px; text-align: center; text-decoration: none; }

  .site-footer { position: absolute; top: 962px; left: 0; width: 1107px; height: 187px; background: var(--footer-bg); text-align: center; }
  .site-footer .brand { left: 50%; top: 17px; transform: translateX(-50%); gap: 6px; }
  .site-footer .brand-dot { width: 40px; height: 40px; background: var(--footer-icon); }
  .site-footer .brand-name { font-size: 22px; color: var(--footer-icon); }
  .footer-nav { position: absolute; top: 69px; left: 0; width: 1107px; font-family: "Roboto", sans-serif; font-size: 14px; color: var(--footer-text); }
  .footer-nav a { color: inherit; text-decoration: none; margin: 0 14px; }
  .call-line { position: absolute; top: 94px; left: 0; width: 1107px; font-family: "Roboto", sans-serif; font-weight: 700; font-size: 19px; color: var(--footer-text); letter-spacing: 0.3px; }
  .social { position: absolute; top: 128px; left: 476px; display: flex; gap: 18px; }
  .social span { width: 35px; height: 35px; background: var(--footer-icon); display: block; }

  .base-bar { position: absolute; top: 1149px; left: 0; width: 1107px; height: 51px; background: var(--base-bar); color: #d8e2ec; font-size: 15px; text-align: center; line-height: 48px; }
</style>
</head>
<body>
  <header class="site-header">
    <div class="brand"><span class="brand-dot"></span><span class="brand-name">Bright Lane</span></div>
    <nav class="main-nav">
      <a href="#">Home</a><span class="divider"></span>
      <a href="#">About</a><span class="divider"></span>
      <a href="#">Network</a><span class="divider"></span>
      <a href="#">Contract</a>
    </nav>
  </header>

  <section class="hero">
    <div class="hero-photo" role="img" aria-label="Photo of a smiling customer support agent wearing a headset, with a colleague softly blurred behind"></div>
    <div class="hero-copy">
      <h1 class="hero-title">You can count on us !</h1>
      <p>Sometimes things are just easier when you know someone in the business. That's where <strong>Bright Lane Collective</strong></p>
      <p>Whether your Air Conditioner is on the fritz, you've got a leaky roof, or need a car salesman you can actually trust..</p>
      <p>Whatever it is, we connect you with Saint Louis' most reputable and affordable solutions, all at <strong>No cost to you!</strong></p>
    </div>
  </section>

  <section class="features">
    <article class="feature" style="left:155px;">
      <svg class="feature-icon" viewBox="0 0 52 52" aria-hidden="true">
        <circle cx="26" cy="26" r="26" fill="var(--brand-blue)"/>
        <rect x="23" y="10" width="6" height="22" rx="2" fill="#fff"/>
        <circle cx="26" cy="39" r="3.5" fill="#fff"/>
      </svg>
      <h2 class="feature-title">About Us</h2>
      <p class="feature-text">The founders of Bright Lane Collective have over 30 years in the St. Louis automotive and HVAC industries. In both markets, among many others, one thing is clear: A consumer gets better service at a lower price when they know who to call.</p>
    </article>
    <a class="read-more" href="#" style="left:220px;">Read more</a>

    <article class="feature" style="left:446px;">
      <svg class="feature-icon" viewBox="0 0 52 52" aria-hidden="true">
        <circle cx="26" cy="26" r="26" fill="var(--brand-blue)"/>
        <path d="M11 26 Q26 13 41 26 Q26 37 11 26 Z" fill="none" stroke="#fff" stroke-width="2.5"/>
        <circle cx="25" cy="25" r="5.5" fill="#fff"/>
      </svg>
      <h2 class="feature-title">Our Vision</h2>
      <p class="feature-text">Bright Lane Collective is now sharing their industry connections with everyone. It's no longer necessary to have a friend or family member in the business to get the service and prices you deserve.</p>
    </article>
    <a class="read-more" href="#" style="left:513px;">Read more</a>

    <article class="feature" style="left:705px;">
      <svg class="feature-icon" viewBox="0 0 52 52" aria-hidden="true">
        <circle cx="26" cy="26" r="26" fill="var(--brand-blue)"/>
        <g fill="#fff">
          <circle cx="19" cy="18" r="3.2"/><path d="M14 27 q5-7 10 0 z"/>
          <circle cx="33" cy="18" r="3.2"/><path d="M28 27 q5-7 10 0 z"/>
          <circle cx="26" cy="31" r="3.2"/><path d="M21 40 q5-7 10 0 z"/>
        </g>
      </svg>
      <h2 class="feature-title">Our Network</h2>
      <ul class="service-list" style="margin-left:36px;">
        <li>Heating</li>
        <li>Air Conditioning</li>
        <li>Automotive Maintenance</li>
        <li>Automotive Sales</li>
        <li>Homse Repair</li>
        <li>Painting</li>
        <li>Chiropractic</li>
        <li>Carpentry</li>
        <li>Roofing</li>
      </ul>
    </article>
    <a class="read-more" href="#" style="left:780px;">Read more</a>
  </section>

  <footer class="site-footer">
    <div class="brand"><span class="brand-dot"></span><span class="brand-name">Bright Lane</span></div>
    <nav class="footer-nav"><a href="#">About Us</a> <a href="#" style="margin-left:26px;">Our Vision</a> <a href="#">Our Network</a></nav>
    <p class="call-line">CALL US: 1-555-014-2730</p>
    <div class="social" aria-label="Social links"><span></span><span></span><span></span><span></span></div>
  </footer>
  <div class="base-bar">All Rights Reserved.</div>
</body>
</html>
```